Medical equipment business looking for professional, unique business card

We need a business card design for a durable medical equipment company. We are small but would like our cards to express that we are much bigger. We focus on braces (back, knee, wrist, etc) but also do crutches, rollators, wheelchairs- basically medical equipment that gets you going and back in Action. Our colors are blue and green and our logo has an arrow and use of a "spine". We'd like to express professionalism while being unique.

Industry/Entity Type

Medical Equipment

Contact Information for Business Card

Professional feel but unique. Memorable.

Font styles to use
Serif
Sans Serif
Other font styles liked:
• verdana

Requirements
Must have
• card holders cell#, business phone#, fax#, email, website address, business address, logo
Nice to have
• use of medical/healthcare related descriptive words, items, look
Should not have
• the wrong colors or cartoon characters.

```html
<!DOCTYPE html>
<html lang="en">
<head>
<meta charset="utf-8">
<title>Keel Medical – Business Card</title>
<link href="https://fonts.googleapis.com/css2?family=Open+Sans:wght@400;600;700&display=swap" rel="stylesheet">
<style>
  :root {
    --brand-blue: #0a8fc9;
    --brand-navy: #14456b;
    --brand-green: #8cc63f;
    --ink: #1d1d1d;
    --paper: #ffffff;
    --backdrop: #e6e8ea;
  }
  * { margin: 0; padding: 0; box-sizing: border-box; }
  html, body {
    width: 1200px; height: 900px; overflow: hidden;
    background: var(--backdrop);
    font-family: "Open Sans", Verdana, sans-serif;
  }
  .canvas { position: relative; width: 1200px; height: 900px; }
  .card {
    position: absolute; left: 250px; width: 700px; height: 400px;
    box-shadow: 0 6px 18px rgba(0,0,0,.18);
    overflow: hidden;
  }
  .card--back { top: 30px; background: var(--brand-blue); }
  .card--front { top: 470px; background: var(--paper); }

  .wordmark { display: flex; align-items: center; gap: 12px; }
  .wordmark__dot {
    width: 22px; height: 22px; border-radius: 50%;
    background: var(--brand-green);
  }
  .wordmark__name {
    font-weight: 700; color: var(--brand-navy);
    font-size: 58px; line-height: 1; letter-spacing: -1px;
  }
  .tagline { font-weight: 700; font-size: 19px; }

  .card--back .logo-block {
    position: absolute; left: 0; right: 0; top: 120px;
    display: flex; flex-direction: column; align-items: center;
  }
  .card--back .tagline { color: var(--paper); margin-top: 8px; }
  .card--back .rule { width: 340px; height: 3px; background: var(--brand-green); margin-top: 6px; }
  .card--back .website {
    position: absolute; left: 0; right: 0; top: 300px; text-align: center;
    color: var(--paper); font-size: 18px; letter-spacing: 2px;
  }

  .card--front .logo-block { position: absolute; left: 48px; top: 30px; }
  .card--front .wordmark__name { font-size: 50px; }
  .card--front .tagline { color: var(--brand-blue); font-size: 16px; margin-top: 6px; margin-left: 34px; }
  .card--front .rule { width: 280px; height: 2px; background: var(--brand-green); margin: 4px 0 0 34px; }

  .address {
    position: absolute; left: 70px; top: 142px;
    font-size: 15px; line-height: 1.3; font-style: normal; color: var(--ink);
  }
  .contacts {
    position: absolute; left: 48px; top: 190px; list-style: none;
    font-size: 15px; line-height: 1.3; color: var(--ink);
  }
  .contacts li { display: flex; align-items: center; gap: 8px; }
  .contacts svg { width: 14px; height: 14px; fill: var(--brand-blue); flex: none; }

  .holder { position: absolute; left: 430px; top: 200px; }
  .holder__name { color: var(--brand-blue); font-size: 28px; font-weight: 400; }
  .holder__role { color: var(--ink); font-size: 16px; margin-top: -4px; }

  .swoosh { position: absolute; left: 0; top: 0; width: 700px; height: 400px; }
  .card--front .website {
    position: absolute; right: 40px; bottom: 16px;
    color: var(--paper); font-size: 20px; letter-spacing: 1.5px;
  }
</style>
</head>
<body>
<main class="canvas">

  <section class="card card--back" aria-label="Card back">
    <div class="logo-block">
      <div class="wordmark">
        <span class="wordmark__dot"></span>
        <span class="wordmark__name">Keel Medical</span>
      </div>
      <div class="tagline">Durable Medical Equipment</div>
      <div class="rule"></div>
    </div>
    <p class="website">www.keelmedical.com</p>
  </section>

  <section class="card card--front" aria-label="Card front">
    <svg class="swoosh" viewBox="0 0 700 400" aria-hidden="true">
      <path d="M0 300 C 200 350, 450 350, 700 300 L 700 400 L 0 400 Z" fill="var(--brand-green)"/>
      <path d="M0 306 C 200 354, 450 358, 700 320 L 700 400 L 0 400 Z" fill="var(--paper)"/>
      <path d="M0 312 C 200 360, 450 364, 700 328 L 700 400 L 0 400 Z" fill="var(--brand-blue)"/>
    </svg>

    <div class="logo-block">
      <div class="wordmark">
        <span class="wordmark__dot"></span>
        <span class="wordmark__name">Keel Medical</span>
      </div>
      <div class="tagline">Durable Medical Equipment</div>
      <div class="rule"></div>
    </div>

    <address class="address">
      418 Linden Ave, Suite #2<br>Fairview TN, 37062
    </address>

    <ul class="contacts">
      <li><svg viewBox="0 0 16 16"><path d="M3 1l3 3-1.5 2a9 9 0 0 0 5.5 5.5L12 10l3 3-2 2C7 15 1 9 1 3z"/></svg>(555) 210-4417</li>
      <li><svg viewBox="0 0 16 16"><path d="M4 0h8a1 1 0 0 1 1 1v14a1 1 0 0 1-1 1H4a1 1 0 0 1-1-1V1a1 1 0 0 1 1-1zm1 2v10h6V2z"/></svg>(555) 210-8830</li>
      <li><svg viewBox="0 0 16 16"><path d="M4 0h8v4H4zM1 5h14v7h-3v4H4v-4H1zm5 6v3h4v-3z"/></svg>(555) 640-2291</li>
      <li><svg viewBox="0 0 16 16"><path d="M0 3h16v10H0zm1 1l7 5 7-5v-.01z"/></svg>info@keelmedical.com</li>
    </ul>

    <div class="holder">
      <p class="holder__name">Daniel Hollis</p>
      <p class="holder__role">Manager</p>
    </div>

    <p class="website">www.keelmedical.com</p>
  </section>

</main>
</body>
</html>
```